Electronic Music Artist needs an Album Cover

DRELL is an electronic musician from Boston, Massachusetts. He needs an album cover that captures the essence of his music. The album is called Lanterns, which represents his experiences growing up, positive and negative. He would like to see designs that involves color and creativity. Attached are some examples of artworks that DRELL likes. He also included a few of his original photos (optional to use. Using a photo will not effect his final decision!), and his logo.

Colors

Designer to choose colors to be used in the design.

Requirements
Must have
• My project must have the text "Lanterns" and "DRELL", and the logo (attached in the files). The logo should not be the main subject of the artwork. Everything must look aesthetically pleasing.
Nice to have
• It would be nice to have some sort of creative graphic design (see example album covers for reference). Also, in one of the references, there is a column on the left hand side with some text in it. That could be cool to include, but without the asian text.
Should not have
• The project should not have any other language besides English.

```html
<!DOCTYPE html>
<html lang="en">
<head>
<meta charset="utf-8">
<title>DRELL – Lanterns</title>
<link rel="stylesheet" href="https://fonts.googleapis.com/css2?family=Archivo+Black&family=Roboto+Condensed:wght@300&family=Libre+Baskerville:wght@700&display=swap">
<style>
  :root {
    --green: #66bd45;
    --yellow: #e9e71c;
    --red: #ec1c24;
  }
  html, body {
    margin: 0;
    padding: 0;
    width: 1200px;
    height: 1200px;
    overflow: hidden;
    background: var(--yellow);
  }
  .album-cover {
    position: relative;
    width: 1200px;
    height: 1200px;
    overflow: hidden;
  }
  .stripe-artwork {
    position: absolute;
    inset: 0;
    background:
      radial-gradient(ellipse 55% 40% at 50% 50%, rgba(233,231,28,0.55), rgba(233,231,28,0) 70%),
      repeating-linear-gradient(180deg, var(--green) 0 26px, var(--yellow) 26px 52px);
    opacity: 1;
  }
  .stripe-artwork::after {
    content: "";
    position: absolute;
    inset: 0;
    background: linear-gradient(90deg, rgba(102,189,69,0.35), rgba(233,231,28,0.15) 50%, rgba(102,189,69,0.35));
  }
  .artist-mark {
    position: absolute;
    left: 0;
    right: 0;
    top: 84px;
    display: flex;
    flex-direction: column;
    align-items: center;
    gap: 22px;
  }
  .artist-mark__square {
    width: 46px;
    height: 46px;
    background: var(--red);
  }
  .artist-mark__name {
    font-family: "Roboto Condensed", sans-serif;
    font-weight: 300;
    font-size: 38px;
    letter-spacing: 2px;
    color: var(--red);
    line-height: 1;
  }
  .album-title {
    position: absolute;
    left: 0;
    top: 0;
    width: 1200px;
    height: 1200px;
  }
  .album-title text {
    font-family: "Archivo Black", sans-serif;
    fill: var(--red);
  }
  .tracklist {
    position: absolute;
    left: 56px;
    top: 928px;
    margin: 0;
    padding: 0;
    list-style: none;
    font-family: "Roboto Condensed", sans-serif;
    font-weight: 300;
    font-size: 14px;
    line-height: 17.8px;
    color: var(--red);
  }
</style>
</head>
<body>
  <main class="album-cover">
    <div class="stripe-artwork" role="img" aria-label="Mirrored psychedelic pattern of wavy green and yellow stripes filling the cover"></div>

    <header class="artist-mark">
      <div class="artist-mark__square"></div>
      <div class="artist-mark__name">DRELL</div>
    </header>

    <svg class="album-title" viewBox="0 0 1200 1200" aria-label="Lanterns">
      <text x="52" y="699" font-size="268" textLength="1106" lengthAdjust="spacingAndGlyphs">LANTERNS</text>
    </svg>

    <ol class="tracklist">
      <li>01.differnces are good</li>
      <li>02. see you when I get there</li>
      <li>03. hardboiled wonderland and the edge of the world</li>
      <li>04. because I am not sure about the songs</li>
      <li>05. looking forward to hearing your music</li>
      <li>06. would make the designprocess even more fun</li>
      <li>07. just making things up as I go</li>
      <li>08. unleash the dog</li>
      <li>09. I am running out off words</li>
      <li>10. this is how we do it</li>
      <li>11. intergalactic</li>
    </ol>
  </main>
</body>
</html>
```